Clean and modern business cards

Looking for an updated business card design for my dental office “corvanta dental” . Looking for a modern clean / sleek design . I’m thinking black background but open to seeing other options . One side needs to have an appointment card . Card needs to have logo, dentist name , phone, email , address . I’ve attached couple of cards I thought were cool as well as my logo
Target Market(s)
Dental patients
Industry/Entity Type
Dentistry
Contact Information for Business Card
Phone email address

```html
<!DOCTYPE html>
<html lang="en">
<head>
<meta charset="utf-8">
<title>Corvanta Dental – Business Card</title>
<link rel="stylesheet" href="https://fonts.googleapis.com/css2?family=Montserrat:wght@600;700&family=Raleway:wght@400&family=Catamaran:wght@500;600&display=swap">
<style>
  :root {
    --backdrop: #d5d6d8;
    --card: #000000;
    --ink: #f0f0f0;
    --gold: #d9aa0a;
    --teal: #0a8aa6;
    --green: #86a80a;
  }
  * { box-sizing: border-box; margin: 0; padding: 0; }
  html, body { width: 1200px; height: 1200px; overflow: hidden; }
  body { background: var(--backdrop); position: relative; }

  .card {
    position: absolute;
    left: 206px;
    width: 787px;
    height: 450px;
    background: var(--card);
    overflow: hidden;
    box-shadow: 0 6px 24px rgba(0,0,0,0.25);
  }
  .card--front { top: 125px; }
  .card--back { top: 623px; }

  .brand-band {
    position: absolute; left: 0; right: 0; bottom: 0; height: 11px;
    display: flex;
  }
  .brand-band span { flex: 1; }
  .brand-band .gold { background: var(--gold); }
  .brand-band .teal { background: var(--teal); }
  .brand-band .green { background: var(--green); }

  .brand-dot {
    position: absolute; width: 150px; height: 150px; border-radius: 50%;
    background: var(--teal);
  }
  .brand-name {
    position: absolute;
    font-family: "Montserrat", sans-serif; font-weight: 700;
    color: var(--ink); text-align: right; line-height: 1;
  }
  .brand-name .word { display: block; font-size: 62px; letter-spacing: -1px; }
  .brand-name .sub { display: block; font-size: 27px; letter-spacing: 11px; margin-top: 14px; margin-right: -11px; }

  .card--front .brand-dot { left: 150px; top: 60px; }
  .card--front .brand-name { right: 132px; top: 136px; transform: translateY(-50%); }

  .dentist-name {
    position: absolute; left: 38px; top: 277px;
    font-family: "Montserrat", sans-serif; font-weight: 600;
    font-size: 38px; letter-spacing: -1.8px; color: var(--gold); line-height: 1;
  }
  .name-rule {
    position: absolute; left: 451px; width: 295px; top: 294px; height: 2px; background: var(--ink);
  }
  .contact-list, .address {
    position: absolute; top: 330px; list-style: none;
    font-family: "Raleway", sans-serif; font-weight: 400; font-size: 22px;
    color: var(--ink); line-height: 30.5px;
  }
  .contact-list { left: 38px; }
  .contact-list li { display: flex; align-items: center; gap: 14px; }
  .contact-list svg { width: 20px; height: 20px; flex: none; }
  .address { right: 39px; text-align: right; }

  .backdrop-glow {
    position: absolute; left: 300px; top: 0; width: 487px; height: 439px;
    background:
      radial-gradient(circle at 70% 45%, rgba(10,138,166,0.22), transparent 45%),
      radial-gradient(circle at 40% 70%, rgba(217,170,10,0.16), transparent 40%),
      radial-gradient(circle at 85% 80%, rgba(134,168,10,0.18), transparent 35%),
      radial-gradient(circle at 55% 20%, rgba(120,40,140,0.18), transparent 35%);
  }
  .card--back .brand-dot { left: 145px; top: 42px; }
  .card--back .brand-name { right: 118px; top: 96px; transform: translateY(-50%); z-index: 1; }

  .appointment {
    position: absolute; left: 0; right: 0; z-index: 1;
    font-family: "Catamaran", sans-serif; color: var(--ink);
  }
  .appointment-title {
    position: absolute; top: 232px; left: 0; right: 0; text-align: center;
    font-weight: 600; font-size: 25px;
  }
  .appointment-fields {
    position: absolute; top: 284px; left: 57px; width: 675px;
    display: flex; align-items: baseline;
    font-weight: 600; font-size: 25px;
  }
  .appointment-fields .leader { border-bottom: 3px dotted var(--ink); height: 1px; align-self: flex-end; margin-bottom: 7px; }
  .appointment-fields .leader--date { width: 230px; }
  .appointment-fields .leader--time { flex: 1; }
  .appointment-note {
    position: absolute; top: 352px; left: 0; right: 0; text-align: center;
    font-weight: 500; font-size: 23px; line-height: 32px; color: var(--green);
  }
</style>
</head>
<body>

<section class="card card--front" aria-label="Business card front">
  <div class="brand-dot"></div>
  <div class="brand-name"><span class="word">CORVANTA</span><span class="sub">DENTAL</span></div>

  <h1 class="dentist-name">DR. ELIAS VARNEK</h1>
  <div class="name-rule"></div>

  <ul class="contact-list">
    <li>
      <svg viewBox="0 0 24 24" aria-hidden="true"><path fill="none" stroke="#86a80a" stroke-width="2.2" stroke-linecap="round" stroke-linejoin="round" d="M6 3l3 4-2 2c1 3 4 6 7 7l2-2 4 3-2 3C10 20 4 14 3 5z"/></svg>
      (204) 555-0193
    </li>
    <li>
      <svg viewBox="0 0 24 24" aria-hidden="true"><rect x="2" y="5" width="20" height="14" fill="#86a80a"/><path d="M2 5l10 8 10-8M2 19l8-7M22 19l-8-7" fill="none" stroke="#000" stroke-width="1.5"/></svg>
      HELLO@CORVANTAWPG.CA
    </li>
    <li>
      <svg viewBox="0 0 24 24" aria-hidden="true"><circle cx="12" cy="12" r="10" fill="none" stroke="#86a80a" stroke-width="2"/><path d="M7 6c2 1 2 3 4 3s1 3-1 4-2 4-1 6M15 4c0 2 2 3 3 5M14 15c2 0 3 2 3 4" fill="none" stroke="#86a80a" stroke-width="2"/></svg>
      CORVANTAWPG.CA
    </li>
  </ul>

  <address class="address">2380 LARKSPUR<br>HWY, WINNIPEG,<br>MB</address>

  <div class="brand-band"><span class="gold"></span><span class="teal"></span><span class="green"></span></div>
</section>

<section class="card card--back" aria-label="Appointment card">
  <div class="backdrop-glow" role="img" aria-label="Soft multicoloured glow decoration in the background"></div>
  <div class="brand-dot"></div>
  <div class="brand-name"><span class="word">CORVANTA</span><span class="sub">DENTAL</span></div>

  <div class="appointment">
    <p class="appointment-title">Your Next Appointment is</p>
    <div class="appointment-fields">
      <span>Date</span><span class="leader leader--date"></span>
      <span>Time</span><span class="leader leader--time"></span>
    </div>
    <p class="appointment-note">To cancel or reschedule please notify us at least<br>48 hours prior to your scheduled appointment</p>
  </div>

  <div class="brand-band"><span class="gold"></span><span class="teal"></span><span class="green"></span></div>
</section>

</body>
</html>
```